Communication Skill: GLOW Bridge

I need a Design for a skill I teach to youth. That's why the title GLOW Bridge. GLOW stands for Thoughts, Emotions, Concerns, Hopes & Desires. Under each word are some examples that are meant to help people discuss certain things. I tried to create something myself but want something much more creative and dynamic. I have attached what I designed because it has the information I need in the design. Want it to have a techie look to it.

```html
<!DOCTYPE html>
<html lang="en">
<head>
<meta charset="utf-8">
<title>GLOW Bridge – Communication Skill</title>
<link href="https://fonts.googleapis.com/css2?family=Anton&family=Oswald:wght@600&family=Nunito+Sans:wght@400&display=swap" rel="stylesheet">
<style>
  :root {
    --bg-centre: #ffffff;
    --bg-edge: #e6e6e6;
    --navy: #3a4ab0;
    --hopes: #3a97d4;
    --hopes-text: #1f7ab8;
    --thoughts: #9459b3;
    --thoughts-text: #8a45ad;
    --emotions: #f2865a;
    --emotions-text: #e8673c;
    --concerns: #e24b3b;
    --concerns-text: #e04535;
    --red: #e22a2e;
    --teal: #6fb6b1;
    --yellow: #f3bb1a;
    --steel-blue: #4a93cf;
    --dot-grey: #444;
  }
  * { margin: 0; padding: 0; box-sizing: border-box; }
  html, body { width: 1200px; height: 977px; overflow: hidden; }
  body {
    background: radial-gradient(ellipse at 50% 45%, var(--bg-centre) 30%, var(--bg-edge) 100%);
  }
  .board { position: relative; width: 1200px; height: 977px; }
  .board svg { position: absolute; inset: 0; }
  .title {
    font-family: "Anton", "Oswald", sans-serif;
    fill: var(--navy);
  }
  .topic-label {
    font-family: "Oswald", sans-serif;
    font-weight: 600;
    font-size: 28px;
    text-anchor: middle;
  }
  .phrases {
    font-family: "Nunito Sans", "Helvetica Neue", sans-serif;
    font-size: 18.5px;
  }
  .phrases.hopes { fill: var(--hopes-text); }
  .phrases.thoughts { fill: var(--thoughts-text); }
  .phrases.emotions { fill: var(--emotions-text); }
  .phrases.concerns { fill: var(--concerns-text); }
  .rule { fill: none; stroke-width: 2.2; stroke-linecap: round; }
  .dash { stroke-dasharray: 4 3; }
</style>
</head>
<body>
<main class="board">
<svg viewBox="0 0 1200 977" width="1200" height="977" aria-label="GLOW Bridge: thoughts, emotions, concerns, hopes and desires">
  <defs>
    <radialGradient id="tone-hopes"><stop offset="55%" stop-color="#fff"/><stop offset="100%" stop-color="var(--hopes)"/></radialGradient>
    <radialGradient id="tone-thoughts"><stop offset="55%" stop-color="#fff"/><stop offset="100%" stop-color="var(--thoughts)"/></radialGradient>
    <radialGradient id="tone-emotions"><stop offset="55%" stop-color="#fff"/><stop offset="100%" stop-color="var(--emotions)"/></radialGradient>
    <radialGradient id="tone-concerns"><stop offset="55%" stop-color="#fff"/><stop offset="100%" stop-color="var(--concerns)"/></radialGradient>
  </defs>

  <!-- rules beside the prompts -->
  <g class="rules">
    <path class="rule" stroke="var(--hopes)" d="M572,43 V146"/>
    <circle cx="572" cy="43" r="4.5" fill="var(--hopes)"/>

    <path class="rule" stroke="var(--thoughts)" d="M848,183 V287"/>
    <circle cx="848" cy="287" r="4.5" fill="var(--thoughts)"/>
    <path class="rule" stroke="var(--thoughts)" d="M1110,176 V255"/>
    <circle cx="1110" cy="255" r="5.5" fill="var(--thoughts)"/>

    <path class="rule" stroke="var(--emotions)" d="M89,612 V846"/>
    <circle cx="89" cy="612" r="6" fill="var(--emotions)"/>
    <path class="rule" stroke="var(--emotions)" d="M394,730 V833"/>
    <circle cx="394" cy="730" r="4.5" fill="var(--emotions)"/>

    <path class="rule dash" stroke="var(--concerns)" d="M523,716 V917"/>
    <circle cx="523" cy="716" r="6" fill="var(--concerns)"/>
    <path class="rule" stroke="var(--concerns)" d="M828,819 V921"/>
    <circle cx="828" cy="819" r="4.5" fill="var(--concerns)"/>
  </g>

  <!-- title frame -->
  <g class="title-frame">
    <path class="rule dash" stroke="var(--navy)" d="M860,352 H193 A65,65 0 0 0 193,482 H477"/>
    <path class="rule" stroke="var(--navy)" d="M477,482 H866"/>
    <circle cx="860" cy="352" r="5" fill="var(--dot-grey)"/>
  </g>

  <!-- small accent artwork areas -->
  <g class="accents">
    <circle role="img" aria-label="Small red gear illustration" cx="326" cy="289" r="49" fill="var(--red)"/>
    <circle role="img" aria-label="Small teal gear illustration" cx="469" cy="301" r="37" fill="var(--teal)"/>
    <circle role="img" aria-label="Small yellow gear illustration" cx="373" cy="552" r="57" fill="var(--yellow)"/>
    <circle role="img" aria-label="Small blue gear illustration" cx="629" cy="532" r="37" fill="var(--steel-blue)"/>
    <circle role="img" aria-label="Small orange gear illustration" cx="969" cy="577" r="58" fill="var(--emotions)"/>
    <circle role="img" aria-label="Small teal gear illustration" cx="1037" cy="662" r="43" fill="var(--teal)"/>
  </g>

  <!-- topic artwork areas with labels -->
  <g class="topic hopes">
    <circle role="img" aria-label="Blue gear illustration for hopes" cx="689" cy="241" r="100" fill="url(#tone-hopes)"/>
    <text class="topic-label" x="689" y="252" fill="var(--hopes-text)">HOPES</text>
  </g>
  <g class="topic thoughts">
    <circle role="img" aria-label="Purple gear illustration for thoughts" cx="973" cy="350" r="100" fill="url(#tone-thoughts)"/>
    <text class="topic-label" x="973" y="361" fill="var(--thoughts-text)">THOUGHTS</text>
  </g>
  <g class="topic emotions">
    <circle role="img" aria-label="Orange gear illustration for emotions" cx="221" cy="623" r="98" fill="url(#tone-emotions)"/>
    <text class="topic-label" x="223" y="634" fill="var(--emotions-text)">EMOTIONS</text>
  </g>
  <g class="topic concerns">
    <circle role="img" aria-label="Red gear illustration for concerns" cx="667" cy="718" r="101" fill="url(#tone-concerns)"/>
    <text class="topic-label" x="667" y="729" fill="var(--concerns-text)">CONCERNS</text>
  </g>

  <!-- title -->
  <text class="title" x="173" y="461" font-size="112" textLength="671" lengthAdjust="spacingAndGlyphs">GLOW BRIDGE</text>

  <!-- phrase prompts -->
  <g class="phrases hopes">
    <text x="590" y="64">I hope..<tspan x="674">I wish..</tspan></text>
    <text x="590" y="88">It’s my desire..<tspan x="725">I’d like to see..</tspan></text>
    <text x="590" y="112">I want..<tspan x="679">I need..</tspan></text>
  </g>
  <g class="phrases thoughts">
    <text x="866" y="175">It seems…<tspan x="974">I wonder…</tspan></text>
    <text x="866" y="200">It’s my opinion..<tspan x="1019">I believe..</tspan></text>
    <text x="866" y="224">I assume..<tspan x="969">I think..</tspan></text>
  </g>
  <g class="phrases emotions">
    <text x="104" y="762">I’m…<tspan x="202">hopeful</tspan><tspan x="294">worried</tspan></text>
    <text x="104" y="786">sad<tspan x="166">afraid</tspan><tspan x="252">mad</tspan><tspan x="321">glad</tspan></text>
    <text x="104" y="811">happy<tspan x="179">confident</tspan><tspan x="287">insecure</tspan></text>
    <text x="104" y="835">lonely<tspan x="182">bothered</tspan><tspan x="278">uncertain</tspan></text>
  </g>
  <g class="phrases concerns">
    <text x="541" y="864">I worry about..<tspan x="687">I’m afraid that..</tspan></text>
    <text x="541" y="888">I’m nervous because..</text>
    <text x="541" y="912">It bothers me that..</text>
  </g>
</svg>
</main>
</body>
</html>
```